【ワイヤーフレーム】
http://kovexa.hostmir.example/client-check/lumera/waiya.png
※極力ワイヤーフレームにそって作成して下さい。

【画像について】
各メニューに配置する写真とメインイメージの写真をお纏め致しました。
必ずこの写真を配置して下さい★
https://19.filevault.example/0827-3c7e1a9f40b2d65e8814a0c9f7d31b62

【今のサイトの問題点】
・何のメニューか分かりづらい
・鍼、カリオンの強みが弱い
・サイトからのお問い合わせが全くない

【TOPデザイン作成にあたっての要望】
・予約アイコンをつける
・ファイシャルメニューが一番売りたいメニューとなります。
デザインは目立つように作成して下さい。
・針、カリオン併用治療を押したい
・高級街にあるので高級感があるデザイン
・ピクセルノート、スナップロウのアイコンを配置する

【ターゲット】
・新規顧客さま
会社員、主婦、お金もっている30代~40代

【サイトの目的】
・集客
・店舗の強みの打ち出し

【サイトマップ】
①TOP
②ABOUT US スタッフ
③トータルビューティー
④フェイシャルビュティー
⑤インナービュティー
⑥コラーゲンマシーン
⑦遺伝子検査・腸内フローラ
⑧料金表
⑨メニュー内容
⑩ニュース一覧
⑪ニュース詳細
⑫ブログ一覧
⑬ブログ詳細
⑭鍼・カリオンの説明
⑮よくある質問
⑯アクセス、治療時間、お問い合わせ
⑰求人(非表示 ページには設けなくていいです)
⑱物販 (非表示 ページには設けなくていいです)
⑲実績
⑳お客様の声

【カラー】
・茶色
・グレー

【参考サイト】
https://www.velkanis.example/ https://moravel-co.example
https://www.lumera1954.example/
茶系、グレー系
【ワイヤーフレーム】
※極力ワイヤーフレームにそって作成して下さい。

【画像について】
必ずこの写真を配置して下さい★
暗めの印象で作成をお願い致します。
濃い色味7:明るい色味3
今回4日間だけ延長させて頂きます。

この度はたくさんの応募有難うございます。

またの機会に是非宜しくお願い致します!

```html
<!DOCTYPE html>
<html lang="ja">
<head>
<meta charset="utf-8">
<title>Lumera Care &amp; Beauty</title>
<link rel="stylesheet" href="https://fonts.googleapis.com/css2?family=Cormorant+Garamond:wght@400;500&family=Noto+Serif+JP:wght@400;500&family=Noto+Sans+JP:wght@400;500&display=swap">
<style>
:root{
  --brown-dark:#2e1c12;
  --brown:#3d2618;
  --brown-mid:#5a3a25;
  --gold:#b8955f;
  --rust:#b4542c;
  --cream:#f6f1ec;
  --paper:#ffffff;
  --text:#3a2a20;
  --muted:#8c7c70;
  --line:#d9cfc5;
}
*{margin:0;padding:0;box-sizing:border-box}
html,body{width:1200px;height:4280px;overflow:hidden}
body{font-family:"Noto Sans JP",sans-serif;color:var(--text);background:var(--brown);position:relative}
.abs{position:absolute}
.serif{font-family:"Noto Serif JP",serif}
.latin{font-family:"Cormorant Garamond",serif;letter-spacing:.12em}
.ph{position:absolute}
p.body{font-size:11px;line-height:1.9}

/* hero */
.hero{position:absolute;left:0;top:0;width:1200px;height:500px;background:linear-gradient(90deg,#f7f3ef 0%,#fbf8f5 40%,#efe5dc 100%)}
.hero .photo{left:430px;top:0;width:770px;height:500px;background:radial-gradient(ellipse at 62% 45%,#ecd7c6 0%,#e2c4ad 30%,#f3ece4 62%,rgba(247,243,239,0) 80%)}
.logo{display:flex;align-items:center;gap:8px;color:var(--brown-mid)}
.logo .mark{width:12px;height:12px;border-radius:50%;background:var(--gold)}
.logo .name{font-family:"Cormorant Garamond",serif;font-size:34px;font-weight:500;line-height:1}
.logo .sub{font-family:"Cormorant Garamond",serif;font-size:12px;letter-spacing:.1em;margin-top:4px;display:block}
.hero .copy{left:60px;top:150px;font-family:"Noto Serif JP",serif;font-size:31px;line-height:1.65;color:var(--brown-mid);letter-spacing:.06em}
.reserve{background:var(--rust);color:#fff;text-align:center}
.hero .reserve{left:1005px;top:0;width:185px;height:44px;padding-top:5px}
.reserve small{display:block;font-size:9px}
.reserve b{font-family:"Cormorant Garamond",serif;font-size:20px;font-weight:500;letter-spacing:.05em}

/* nav */
.nav{position:absolute;left:0;top:500px;width:1200px;height:40px;background:var(--paper);display:flex;align-items:center;border-bottom:1px solid var(--line)}
.nav ul{list-style:none;display:flex;gap:34px;margin-left:252px;font-size:10px;color:var(--text)}
.nav .sns{display:flex;gap:8px;margin-left:26px}
.nav .sns span{width:16px;height:16px;border-radius:50%;background:#9b8b80}
.nav .reserve{margin-left:auto;margin-right:20px;width:150px;height:26px;font-size:11px;line-height:26px;background:var(--brown-mid)}

/* menu */
.menu{position:absolute;left:0;top:540px;width:1200px;height:1080px;background:var(--brown)}
.sec-title{text-align:center;font-family:"Cormorant Garamond",serif;font-size:28px;letter-spacing:.18em;color:#fff}
.sec-title::after{content:"";display:block;width:40px;height:1px;background:var(--gold);margin:8px auto 0}
.menu .sec-title{position:absolute;top:72px;width:100%}
.feature h3{font-family:"Noto Serif JP",serif;font-weight:400;font-size:19px;color:#fff;letter-spacing:.08em;border-bottom:1px solid var(--gold);padding-bottom:8px;margin-bottom:14px}
.feature p{color:#d9cbbd}
.more{display:inline-block;border:1px solid #c9b69c;color:#fff;font-size:10px;letter-spacing:.12em;width:150px;height:34px;line-height:32px;text-align:center;margin-top:18px}
.more.dark{border-color:var(--brown-mid);color:var(--brown-mid)}
.card{position:absolute;top:1240px;width:232px}
.card .img{height:150px}
.card h4{font-family:"Noto Serif JP",serif;font-weight:400;font-size:13px;color:#fff;margin:12px 0 6px;border-bottom:1px solid var(--gold);padding-bottom:6px}
.card p{color:#d9cbbd;font-size:10px;line-height:1.8}
.card .more{width:120px;height:28px;line-height:26px;margin-top:10px}

/* acupuncture */
.acu{position:absolute;left:0;top:1620px;width:1200px;height:380px;background:var(--paper)}
.acu h2{font-family:"Noto Serif JP",serif;font-weight:400;font-size:22px;color:var(--brown-mid);letter-spacing:.06em}

/* movie */
.movie{position:absolute;left:0;top:2000px;width:1200px;height:620px;background:linear-gradient(180deg,#3b2618 0%,#5a3c29 50%,#2f1d12 100%)}
.movie .label{left:240px;top:60px;font-family:"Cormorant Garamond",serif;font-size:58px;color:rgba(255,255,255,.28);letter-spacing:.1em}
.movie .frame{left:240px;top:90px;width:720px;height:460px;background:linear-gradient(135deg,#8a6048 0%,#c59a7c 45%,#6b4430 100%)}
.movie .play{left:575px;top:295px}

/* voice */
.voice{position:absolute;left:0;top:2620px;width:1200px;height:460px;background:linear-gradient(180deg,#f3ede7,#faf7f3)}
.voice .sec-title{color:var(--brown-mid);position:absolute;top:50px;width:100%}
.vcard{position:absolute;top:120px;width:350px;height:280px;background:var(--paper);padding:22px 20px;border:1px solid var(--line)}
.tag{display:inline-block;background:var(--rust);color:#fff;font-size:9px;padding:2px 8px}
.vcard h4{font-family:"Noto Serif JP",serif;font-weight:500;font-size:14px;color:var(--brown-mid);margin:10px 0 12px;border-bottom:1px solid var(--line);padding-bottom:10px}
.vcard p{width:190px;font-size:10px;line-height:1.9;color:var(--muted)}
.vcard .img{right:20px;top:100px;width:110px;height:140px}

/* sns */
.sns-sec{position:absolute;left:0;top:3080px;width:1200px;height:540px;background:var(--brown-dark)}
.sns-sec h3{position:absolute;top:50px;width:340px;text-align:center;font-family:"Cormorant Garamond",serif;font-weight:400;font-size:24px;color:#fff;letter-spacing:.14em}
.feed{left:240px;top:110px;width:340px;height:390px;background:#fff;padding:14px}
.feed .head{display:flex;align-items:center;gap:8px;font-size:10px;color:#333}
.feed .head span{width:28px;height:28px;background:#c9b69c}
.grid{left:620px;top:110px;width:340px;display:grid;grid-template-columns:repeat(3,108px);gap:8px}
.grid div{height:108px}

/* access */
.access{position:absolute;left:0;top:3620px;width:1200px;height:320px;background:var(--paper)}
.access .map{left:600px;top:0;width:600px;height:320px;background:linear-gradient(135deg,#ece8e0,#dcd9d2)}
.access p{font-size:10px;line-height:1.9;color:var(--text)}

/* footer */
.footer{position:absolute;left:0;top:3940px;width:1200px;height:340px;background:var(--brown-dark);color:#cdbfb2}
.footer ul{list-style:none;position:absolute;top:50px;font-size:10px;line-height:2.4}
.footer .fsns{left:820px;top:52px;display:flex;gap:8px}
.footer .fsns span{width:20px;height:20px;border-radius:50%;background:#8e7a6b}
.footer .copy{left:0;top:285px;width:100%;text-align:center;font-size:9px;color:#9c8a7c}
.footer .top{left:1165px;top:300px;width:24px;height:24px;background:#6a5040}
</style>
</head>
<body>

<header class="hero">
  <div class="ph photo" role="img" aria-label="メインイメージ:肌の美しい女性と白い花"></div>
  <div class="abs logo" style="left:22px;top:18px">
    <span class="mark"></span>
    <div><span class="name">Lumera</span><span class="sub">Care &amp; Beauty</span></div>
  </div>
  <p class="abs copy">輝いているあなたに<br>もっと輝いてもらいたい<br>という想いから</p>
  <div class="abs reserve"><small>ご予約・お問い合わせ</small><b>03-5820-4417</b></div>
</header>

<nav class="nav">
  <ul><li>HOME</li><li>ABOUT US</li><li>メニュー</li><li>料金表</li><li>NEWS</li><li>ブログ</li><li>よくある質問</li><li>アクセス</li></ul>
  <div class="sns"><span></span><span></span></div>
  <div class="reserve">WEB予約はこちら</div>
</nav>

<section class="menu">
  <h2 class="sec-title">MENU</h2>
  <div class="ph" style="left:240px;top:150px;width:380px;height:225px;background:linear-gradient(135deg,#e9d2bf,#b98a6c)" role="img" aria-label="フェイシャル施術の写真"></div>
  <div class="abs feature" style="left:650px;top:168px;width:310px">
    <h3>フェイシャルビューティー</h3>
    <p class="body">肌本来の力を引き出す丁寧なフェイシャルケアで、透明感とハリのある素肌へ導きます。お一人おひとりの肌状態に合わせた施術をご提案いたします。</p>
    <span class="more">VIEW MORE　›</span>
  </div>
  <div class="abs feature" style="left:240px;top:420px;width:340px">
    <h3>インナービューティー</h3>
    <p class="body">身体の内側から整えることで、外見の美しさも変わります。鍼とカリオンを組み合わせた施術で巡りを整え、健やかな毎日をサポートします。</p>
    <span class="more">VIEW MORE　›</span>
  </div>
  <div class="ph" style="left:640px;top:400px;width:320px;height:240px;background:linear-gradient(135deg,#c79a7a,#7d5038)" role="img" aria-label="背中の施術の写真"></div>

  <div class="card" style="left:240px;top:700px">
    <div class="img" style="background:linear-gradient(135deg,#a0765a,#5e3c28)" role="img" aria-label="トータルビューティーの施術写真"></div>
    <h4>トータルビューティー</h4>
    <p>全身のバランスを整え、美と健康をトータルにサポートするメニューです。</p>
    <span class="more">VIEW MORE　›</span>
  </div>
  <div class="card" style="left:484px;top:700px">
    <div class="img" style="background:linear-gradient(135deg,#d2453a,#7e2620)" role="img" aria-label="コラーゲンマシンの写真"></div>
    <h4>コラーゲンマシン</h4>
    <p>光の力で肌の奥からハリを与え、気になる部分をやさしくケアします。</p>
    <span class="more">VIEW MORE　›</span>
  </div>
  <div class="card" style="left:728px;top:700px">
    <div class="img" style="background:linear-gradient(135deg,#dbe8ee,#8fb3c4)" role="img" aria-label="遺伝子検査の写真"></div>
    <h4>遺伝子検査・腸内フローラ検査</h4>
    <p>体質を知ることで、あなたに合った美容と健康の方法が見えてきます。</p>
    <span class="more">VIEW MORE　›</span>
  </div>
</section>

<section class="acu">
  <h2 class="abs" style="left:240px;top:70px">鍼とカリオンの併用治療とは?</h2>
  <p class="abs body" style="left:240px;top:120px;width:380px">鍼とカリオンを組み合わせることで、それぞれの効果をより高めることができます。血流を促し、代謝を上げることで、お肌と身体の両方を内側から整えていきます。初めての方にも安心して受けていただけるよう丁寧にご説明いたします。</p>
  <span class="abs more dark" style="left:240px;top:220px">VIEW MORE　›</span>
  <div class="ph" style="left:660px;top:70px;width:300px;height:270px;background:linear-gradient(135deg,#f0ddd0,#b68a70)" role="img" aria-label="顔への鍼施術の写真"></div>
</section>

<section class="movie" role="img" aria-label="施術風景の背景写真">
  <div class="ph frame" role="img" aria-label="動画サムネイル:施術を受ける女性"></div>
  <span class="abs label">MOVIE</span>
  <svg class="abs play" width="50" height="50" viewBox="0 0 50 50"><circle cx="25" cy="25" r="23" fill="none" stroke="#fff" stroke-width="2"/><path d="M20 15 L36 25 L20 35Z" fill="#fff"/></svg>
</section>

<section class="voice">
  <h2 class="sec-title">VOICE</h2>
  <div class="vcard" style="left:240px">
    <span class="tag">30代女性・会社員</span>
    <h4>リードテキストリードテキストリードテキスト</h4>
    <p>施術後は肌の明るさが変わり、周りからも褒められるようになりました。スタッフの方の丁寧な説明も安心でした。また通いたいです。</p>
    <div class="ph img" style="background:linear-gradient(160deg,#f1e4da,#d8bba6)" role="img" aria-label="お客様の写真"></div>
  </div>
  <div class="vcard" style="left:610px">
    <span class="tag">40代女性・主婦</span>
    <h4>リードテキストリードテキストリードテキスト</h4>
    <p>鍼は初めてで不安でしたが、痛みもなくリラックスできました。身体が軽くなり、肌の調子も良くなったと感じています。</p>
    <div class="ph img" style="background:linear-gradient(160deg,#f1e4da,#d8bba6)" role="img" aria-label="お客様の写真"></div>
  </div>
</section>

<section class="sns-sec">
  <h3 style="left:240px">PIXELNOTE</h3>
  <h3 style="left:620px">SNAPROW</h3>
  <div class="abs feed">
    <div class="head"><span></span>Lumera Care &amp; Beauty</div>
    <div style="height:170px;margin-top:12px;background:linear-gradient(135deg,#e2cbb8,#9c6f52)" role="img" aria-label="投稿写真:サロンの施術ベッド"></div>
    <p style="font-size:10px;line-height:1.8;color:#555;margin-top:10px">本日もご来店ありがとうございました。ご予約はお気軽にどうぞ。</p>
    <div style="height:110px;margin-top:10px;background:linear-gradient(135deg,#efe6dd,#c9ac95)" role="img" aria-label="投稿写真:花と店内"></div>
  </div>
  <div class="abs grid">
    <div style="background:#a57656" role="img" aria-label="投稿写真"></div>
    <div style="background:#c6a18a" role="img" aria-label="投稿写真"></div>
    <div style="background:#7b4f38" role="img" aria-label="投稿写真"></div>
    <div style="background:#d9c2b0" role="img" aria-label="投稿写真"></div>
    <div style="background:#b23a2e" role="img" aria-label="投稿写真"></div>
    <div style="background:#9a7660" role="img" aria-label="投稿写真"></div>
    <div style="background:#e6d8cc" role="img" aria-label="投稿写真"></div>
    <div style="background:#8c6650" role="img" aria-label="投稿写真"></div>
    <div style="background:#c9b09c" role="img" aria-label="投稿写真"></div>
  </div>
</section>

<section class="access">
  <div class="abs logo" style="left:240px;top:60px">
    <span class="mark"></span>
    <div><span class="name">Lumera</span><span class="sub">Care &amp; Beauty</span></div>
  </div>
  <p class="abs" style="left:240px;top:135px;width:320px">〒104-0061 東京都中央区銀座架空町1-2-3 ルメラビル4F<br>営業時間 10:00〜20:00 / 定休日 火曜日</p>
  <div class="abs reserve" style="left:240px;top:200px;width:160px;height:40px;padding-top:4px"><small>お電話でのご予約</small><b>03-5820-4417</b></div>
  <div class="abs reserve" style="left:410px;top:200px;width:150px;height:40px;line-height:40px;font-size:11px;background:var(--brown-mid)">WEB予約はこちら</div>
  <div class="ph map" role="img" aria-label="店舗周辺の地図"></div>
  <svg class="abs" style="left:890px;top:130px" width="22" height="30" viewBox="0 0 22 30"><path d="M11 0C5 0 0 5 0 11c0 8 11 19 11 19s11-11 11-19C22 5 17 0 11 0z" fill="#d23b2f"/><circle cx="11" cy="11" r="4" fill="#fff"/></svg>
</section>

<footer class="footer">
  <ul style="left:240px"><li>HOME</li><li>ABOUT US</li><li>料金表</li></ul>
  <ul style="left:380px"><li>メニュー</li><li>トータルビューティー</li><li>フェイシャルビューティー</li><li>インナービューティー</li><li>コラーゲンマシン</li><li>遺伝子検査・腸内フローラ</li></ul>
  <ul style="left:540px"><li>鍼・カリオンの説明</li><li>よくある質問</li><li>お客様の声</li></ul>
  <ul style="left:690px"><li>アクセス</li><li>NEWS</li><li>ブログ</li><li>お問い合わせ</li></ul>
  <div class="abs fsns"><span></span><span></span></div>
  <p class="abs copy">© Lumera Care &amp; Beauty. All rights reserved.</p>
  <div class="abs top"></div>
</footer>

</body>
</html>
```